Two Web Banners Needed for children product website! Fun and colorful!

My website is www.brightpebbletrinkets.com.au

I want 2 banners for the home page.

Size: 1920x1080px

Colors I like:
#BBA5D0
#FBF5BC
#F2BBAD

Text:
1) We create unique and meaningful gifts
2) We help you create happy memories

Fonts: provided in link

Brief:
1) I need two banners that showcase my two products on my website. I have images and fonts are included you can use in the files.
2) I want to capture child nature, friendliness and happiness.
3) I have also included samples of what I like
4) It's important to use some of the customer photographs too

Link to files:
https://filedrop-example.net/downloads/a1b2c3d4e5f60718293a4b5c6d7e8f9020220101000000/0f1e2d3c4b5a69788796a5b4c3d2e1f020220101000001/9z8y7x

If link does not work please PM me

Target Market(s)

Parents of children

Industry/Entity Type

Children ecommerce

Font styles to use
Other font styles liked:
• in file

Requirements
Must have
• Clean modern look

```html
<!DOCTYPE html>
<html lang="en">
<head>
<meta charset="UTF-8">
<title>Bright Pebble Trinkets – Unique and Meaningful Gifts</title>
<link href="https://fonts.googleapis.com/css2?family=Allura&family=Open+Sans:wght@600;700;800&display=swap" rel="stylesheet">
<style>
  :root {
    --page: #ffffff;
    --purple: #9b72c6;
    --lilac: #b9a3cf;
    --lilac-soft: #c3b0d8;
    --peach: #f2bbad;
    --cream: #fbf5bc;
    --white: #ffffff;
    --button-text: #8a5bb0;
  }
  * { margin: 0; padding: 0; box-sizing: border-box; }
  html, body {
    width: 1200px; height: 900px; overflow: hidden;
    background: var(--page);
  }
  .banner {
    position: absolute; left: 95px; top: 166px;
    width: 1011px; height: 568px;
    overflow: hidden; background: var(--purple);
  }
  .banner-art { position: absolute; inset: 0; }
  .headline {
    position: absolute; left: 57px; top: 42px;
    color: var(--white);
  }
  .headline-script {
    display: block;
    font-family: "Allura", cursive;
    font-weight: 400;
    font-size: 100px; line-height: 1;
    margin-left: -6px;
  }
  .headline-main {
    display: block; margin-top: 4px;
    font-family: "Open Sans", sans-serif;
    font-weight: 700; font-size: 60px;
    line-height: 62px; letter-spacing: 0.5px;
  }
  .accent { color: var(--peach); }
  .shop-button {
    position: absolute; left: 57px; top: 360px;
    width: 133px; height: 36px; border-radius: 18px;
    background: var(--peach); color: var(--button-text);
    font-family: "Open Sans", sans-serif; font-weight: 600;
    font-size: 13px; text-decoration: none;
    display: flex; align-items: center; justify-content: center;
    box-shadow: 0 2px 4px rgba(90, 50, 120, 0.25);
  }
</style>
</head>
<body>
  <section class="banner">
    <svg class="banner-art" width="1011" height="568" viewBox="0 0 1011 568" xmlns="http://www.w3.org/2000/svg">
      <defs>
        <linearGradient id="girl-photo-tones" x1="0" y1="0" x2="0" y2="1">
          <stop offset="0" stop-color="#f8e6e2"/>
          <stop offset="0.45" stop-color="#f3d2d2"/>
          <stop offset="0.7" stop-color="#e58cb4"/>
          <stop offset="1" stop-color="#d3408f"/>
        </linearGradient>
        <linearGradient id="boy-photo-tones" x1="0" y1="0" x2="1" y2="1">
          <stop offset="0" stop-color="#eef0f3"/>
          <stop offset="0.45" stop-color="#ead9c9"/>
          <stop offset="0.75" stop-color="#d9b9a0"/>
          <stop offset="1" stop-color="#b59a86"/>
        </linearGradient>
      </defs>
      <path class="lower-band" d="M0 352 C200 342 420 372 620 392 C780 400 900 352 1011 340 L1011 568 L0 568 Z" fill="var(--lilac)"/>
      <path class="lower-band-soft" d="M0 420 C200 410 330 440 470 460 L470 568 L0 568 Z" fill="var(--lilac-soft)" opacity="0.5"/>
      <circle class="line-ring-cream" cx="625" cy="-10" r="105" fill="none" stroke="var(--cream)" stroke-width="1.5"/>
      <g class="photo-girl-frame">
        <circle cx="840" cy="168" r="238" fill="var(--white)"/>
        <circle cx="840" cy="168" r="234" fill="url(#girl-photo-tones)" role="img" aria-label="Smiling girl in a pink dress holding a pink chair embroidered with her name"/>
      </g>
      <g class="photo-boy-frame">
        <circle cx="595" cy="436" r="185" fill="var(--white)"/>
        <circle cx="595" cy="436" r="181" fill="url(#boy-photo-tones)" role="img" aria-label="Young boy playing with building bricks at a table beside a chair embroidered with his name"/>
      </g>
      <circle class="line-ring-peach" cx="980" cy="610" r="225" fill="none" stroke="var(--peach)" stroke-width="1.5"/>
      <circle class="line-ring-cream-small" cx="1010" cy="470" r="90" fill="none" stroke="var(--cream)" stroke-width="1.5"/>
    </svg>

    <h1 class="headline">
      <span class="headline-script">We Create</span>
      <span class="headline-main"><span class="accent">UNIQUE</span> AND<br><span class="accent">MEANINGFUL</span><br>GIFTS</span>
    </h1>

    <a class="shop-button" href="https://www.brightpebbletrinkets.com.au">SHOP NOW</a>
  </section>
</body>
</html>
```